New E-Learning Website Design Wanted!

I am creating an E-learning website for those interested in getting certifications in the IT industry.
For example, courses related to BKX, Pellin, RTM certifications and national certifications in the IT industry in Japan will be offered.
You can think of sites such as Pindoval, Fevly, VexaPoint, Bintorum.
But I am targeting industries in Japan at the moment.
Also, I have uploaded screenshots of pages that I think are good.

The company is Solvik Data
I recently got my company logo designed so I attached pdf file to this project brief.
I would appreciate it if you can make the site match the color scheme of the logo.

Target Market(s)

I am targeting individuals as well as large IT companies in Japan

Industry/Entity Type

Education

Coding

Coded - Design and coding required

Number of Pages Required

4 page

Font styles to use
Sans Serif

Colors

Designer to choose colors to be used in the design.

Requirements
Must have
• One top page design
• One course page (https://vexapt.test/courses/pellor-grid-systems)
• One learning page(where the learner can see the video)
• One blog page(https://news.vexapt.test/resources?_ga=2.36414185.89678801.1578174478-594719062.1578174478)
Nice to have
• Pricing page

```html
<!DOCTYPE html>
<html lang="en">
<head>
<meta charset="utf-8">
<title>Solvik Data – IT Courses in Japan</title>
<link href="https://fonts.googleapis.com/css2?family=Montserrat:wght@400;500;600;700;800&display=swap" rel="stylesheet">
<style>
:root{
  --navy:#1e2a5c;
  --coral:#f2575c;
  --ink:#2b2b2b;
  --muted:#7a7a80;
  --line:#e4e4ea;
  --bg:#ffffff;
  --dark:#15171d;
}
*{box-sizing:border-box;margin:0;padding:0}
html,body{width:1200px;height:3124px;overflow:hidden;background:var(--bg);font-family:'Montserrat',sans-serif;color:var(--ink)}
.page{position:relative;width:1200px;height:3124px}
.accent{color:var(--coral)}
.btn{display:inline-block;background:var(--coral);color:#fff;font-weight:600;font-size:13px;padding:10px 34px;border-radius:3px;text-decoration:none}
.btn-dark{background:#222;width:100%;text-align:center}
.section-title{text-align:center;font-size:30px;font-weight:700;color:var(--navy)}

/* header */
.site-nav{position:absolute;top:0;left:0;width:1200px;height:50px;display:flex;align-items:center;padding:0 60px 0 96px;z-index:2}
.brand{display:flex;align-items:center;gap:8px;font-weight:600;font-size:13px;color:var(--navy)}
.brand-mark{width:16px;height:16px;background:var(--navy);border-radius:50%}
.nav-links{margin-left:auto;display:flex;gap:30px;align-items:center;font-size:12px;font-weight:500;color:var(--navy)}
.nav-signup{background:var(--navy);color:#fff;padding:6px 28px;border-radius:2px}

/* hero */
.hero{position:absolute;top:0;left:0;width:1200px;height:460px;background:linear-gradient(100deg,#f4f4f3 0%,#ecebe8 45%,#bfbdb8 75%,#8d8a86 100%)}
.hero-photo{position:absolute;right:0;top:0;width:620px;height:460px;background:linear-gradient(160deg,#dcdad5 0%,#9a9893 55%,#6f6d69 100%);opacity:.55}
.hero-copy{position:absolute;left:100px;top:175px}
.hero-copy h1{font-size:38px;font-weight:800;color:var(--navy)}
.hero-copy p{margin:14px 0 26px;font-size:13px;color:#444}

/* certifications */
.certs{position:absolute;top:460px;left:0;width:1200px;height:860px;border-bottom:1px solid var(--line)}
.certs .section-title{margin-top:82px}
.cert-grid{position:absolute;top:160px;left:192px;display:grid;grid-template-columns:repeat(3,250px);column-gap:38px;row-gap:32px}
.cert-card{height:258px;background:#fff;box-shadow:0 2px 12px rgba(0,0,0,.12);padding:14px 16px;text-align:center}
.cert-image{height:100px;border-radius:2px}
.cert-card h3{margin-top:12px;font-size:12px;font-weight:700;line-height:1.35;color:#222;height:48px}
.cert-meta{display:flex;justify-content:space-between;align-items:center;margin-top:14px;font-size:10px;color:var(--muted)}
.stars{color:#f5a623;font-size:14px;letter-spacing:1px}
.price{font-weight:700;color:#222;font-size:10px}
.certs .btn{position:absolute;top:752px;left:537px}

/* companies */
.companies{position:absolute;top:1320px;left:0;width:1200px;height:300px;border-bottom:1px solid var(--line)}
.companies .section-title{margin-top:62px}
.company-row{position:absolute;top:166px;left:170px;width:860px;display:flex;justify-content:space-between;align-items:center}
.company-name{font-size:30px;font-weight:800;color:#111}

/* plans */
.plans{position:absolute;top:1620px;left:0;width:1200px;height:540px;border-bottom:1px solid var(--line)}
.plans .section-title{margin-top:62px}
.plan-grid{position:absolute;top:160px;left:120px;display:grid;grid-template-columns:repeat(3,300px);column-gap:30px}
.plan-card{height:300px;background:#fff;box-shadow:0 2px 12px rgba(0,0,0,.1);padding:24px 34px;font-size:10px;color:var(--muted);text-align:center}
.plan-card h3{text-align:left;font-size:13px;font-weight:600;color:#333;margin-bottom:12px}
.plan-card.featured h3{color:var(--coral)}
.plan-card p{line-height:1.6;margin-bottom:16px}
.plan-card .btn{padding:9px 0;margin-bottom:16px}
.plan-card ul{list-style:none;line-height:1.6}

/* testimonials */
.testimonials{position:absolute;top:2160px;left:0;width:1200px;height:520px}
.testimonials .section-title{margin-top:66px}
.review-grid{position:absolute;top:148px;left:90px;display:grid;grid-template-columns:repeat(3,330px);column-gap:15px}
.review-card{height:140px;background:#fff;box-shadow:0 2px 12px rgba(0,0,0,.1);padding:16px 18px}
.reviewer{display:flex;align-items:center;gap:14px;margin-bottom:12px}
.avatar{width:52px;height:52px;border-radius:50%;background:linear-gradient(135deg,#c9b6a0,#7b6a5a)}
.reviewer h4{font-size:13px;font-weight:600;color:#222}
.review-card p{font-size:10px;line-height:1.55;color:var(--muted)}
.testimonials .btn{position:absolute;top:352px;left:537px}

/* call to action */
.cta{position:absolute;top:2680px;left:0;width:1200px;height:300px;background:radial-gradient(ellipse at 55% 40%,#3b4049 0%,#22252c 45%,var(--dark) 100%);text-align:center}
.cta h2{margin-top:104px;font-size:32px;font-weight:700;color:#fff}
.cta .btn{margin-top:30px}

/* footer */
.site-footer{position:absolute;top:2980px;left:0;width:1200px;height:144px}
.footer-row{display:flex;align-items:center;padding:38px 100px 0 96px}
.footer-links{margin-left:200px;display:flex;gap:24px;font-size:12px;color:var(--navy)}
.social{margin-left:auto;display:flex;gap:12px;font-size:12px;font-weight:700;color:var(--coral)}
.copyright{text-align:center;font-size:10px;color:#444;margin-top:68px}
</style>
</head>
<body>
<div class="page">

  <section class="hero">
    <div class="hero-photo" role="img" aria-label="Photo of hands typing on a laptop at a bright desk"></div>
    <div class="hero-copy">
      <h1>Best <span class="accent">IT Courses</span> in Japan</h1>
      <p>We Provide best learning experience to become a Software Architect</p>
      <a class="btn" href="#">Get Started</a>
    </div>
  </section>

  <header class="site-nav">
    <div class="brand"><span class="brand-mark"></span>Solvik Data</div>
    <nav class="nav-links">
      <span>Learning</span><span>Blog</span><span>Course Sales</span><span>Subscription</span><span>Sign in</span>
      <span class="nav-signup">Sign Up</span>
    </nav>
  </header>

  <section class="certs">
    <h2 class="section-title">National <span class="accent">Certifications</span></h2>
    <div class="cert-grid">
      <article class="cert-card">
        <div class="cert-image" role="img" aria-label="Course cover for the IT Passport exam" style="background:linear-gradient(135deg,#e8eef8,#9fb9e6)"></div>
        <h3>Information Technology Passport Examination</h3>
        <div class="cert-meta"><span class="stars">★★★★☆</span><span class="price">5000 JPY</span></div>
      </article>
      <article class="cert-card">
        <div class="cert-image" role="img" aria-label="Course cover for the information security management exam" style="background:linear-gradient(135deg,#e0457a,#8a2a86)"></div>
        <h3>Information Security Management Examination</h3>
        <div class="cert-meta"><span class="stars">★★★★☆</span><span class="price">5000 JPY</span></div>
      </article>
      <article class="cert-card">
        <div class="cert-image" role="img" aria-label="Course cover for the fundamental engineer exam" style="background:linear-gradient(135deg,#f6f6f6,#dcdcdc)"></div>
        <h3>Fundamental Information Technology Engineer Examination</h3>
        <div class="cert-meta"><span class="stars">★★★★☆</span><span class="price">5000 JPY</span></div>
      </article>
      <article class="cert-card">
        <div class="cert-image" role="img" aria-label="Course cover for the applied engineer exam" style="background:linear-gradient(135deg,#79c9e8,#2f7fb8)"></div>
        <h3>Applied Information Technology Engineer Examination</h3>
        <div class="cert-meta"><span class="stars">★★★★☆</span><span class="price">5000 JPY</span></div>
      </article>
      <article class="cert-card">
        <div class="cert-image" role="img" aria-label="Course cover for the database specialist exam" style="background:linear-gradient(135deg,#2b2e3a,#c8b15a)"></div>
        <h3>Database Specialist Examination</h3>
        <div class="cert-meta"><span class="stars">★★★★☆</span><span class="price">5000 JPY</span></div>
      </article>
      <article class="cert-card">
        <div class="cert-image" role="img" aria-label="Course cover for the registered security specialist exam" style="background:linear-gradient(135deg,#e23a3a,#b01d2c)"></div>
        <h3>Registered Information Security Specialist Examination</h3>
        <div class="cert-meta"><span class="stars">★★★★☆</span><span class="price">5000 JPY</span></div>
      </article>
    </div>
    <a class="btn" href="#">Get Started</a>
  </section>

  <section class="companies">
    <h2 class="section-title">Get Hired at <span class="accent">Top Companies</span></h2>
    <div class="company-row">
      <span class="company-name">Kadora</span>
      <span class="company-name">Mirel</span>
      <span class="company-name">Vantoly</span>
      <span class="company-name">Strada</span>
      <span class="company-name">Brenvo</span>
      <span class="company-name">Lumeque</span>
    </div>
  </section>

  <section class="plans">
    <h2 class="section-title">Choose <span class="accent">Subscription Plan</span></h2>
    <div class="plan-grid">
      <article class="plan-card">
        <h3>Programming</h3>
        <p>Core coding tracks with weekly practice sets, guided projects and short quizzes that help you build solid habits and pass your first exam with ease.</p>
        <a class="btn btn-dark" href="#">Get Started</a>
        <ul><li>Monthly plan</li><li>Cancel at any time</li><li>Certificate on completion</li></ul>
      </article>
      <article class="plan-card">
        <h3>Cloud</h3>
        <p>Cloud tracks covering setup, networking and security, with hands-on labs and mock tests built for the certifications most sought by employers.</p>
        <a class="btn btn-dark" href="#">Get Started</a>
        <ul><li>Monthly plan</li><li>Cancel at any time</li><li>Certificate on completion</li></ul>
      </article>
      <article class="plan-card featured">
        <h3>ALL IN ONE</h3>
        <p>Every course in one plan, including national exams, coding and cloud tracks, with mentor support and new lessons added each month.</p>
        <a class="btn" style="width:100%;padding:9px 0;margin-bottom:16px" href="#">Get Started</a>
        <ul><li>Yearly plan</li><li>Mentor support</li><li>All certificates</li></ul>
      </article>
    </div>
  </section>

  <section class="testimonials">
    <h2 class="section-title">What <span class="accent">Our Students</span> Have to Say</h2>
    <div class="review-grid">
      <article class="review-card">
        <div class="reviewer"><div class="avatar" role="img" aria-label="Student portrait"></div><h4>Tanabe Kazuo</h4></div>
        <p>The lessons were clear and the mock exams felt just like the real test. I passed on my first try and moved to a new role.</p>
      </article>
      <article class="review-card">
        <div class="reviewer"><div class="avatar" role="img" aria-label="Student portrait"></div><h4>Morikawa Hiro</h4></div>
        <p>Short videos fit my schedule after work. The practice sets showed me exactly where to focus before the exam day came.</p>
      </article>
      <article class="review-card">
        <div class="reviewer"><div class="avatar" role="img" aria-label="Student portrait"></div><h4>Ishida Ren</h4></div>
        <p>Great support from mentors and a tidy course layout. I earned two certifications this year and feel ready for more.</p>
      </article>
    </div>
    <a class="btn" href="#">Get Started</a>
  </section>

  <section class="cta" role="img" aria-label="Dark photo of a person working at a computer">
    <h2>Ensure Your <span class="accent">Career</span> and <span class="accent">Future</span></h2>
    <a class="btn" href="#">Get Started</a>
  </section>

  <footer class="site-footer">
    <div class="footer-row">
      <div class="brand"><span class="brand-mark"></span>Solvik Data</div>
      <nav class="footer-links">
        <span>Learning</span><span>Blog</span><span>Course Sales</span><span>Subscription</span><span>Sign In</span><span>Sign Up</span>
      </nav>
      <div class="social"><span>Kivo</span><span>Lunet</span><span>Tweza</span></div>
    </div>
    <p class="copyright">Copyright © 2020 Solvik Data</p>
  </footer>

</div>
</body>
</html>
```